Wesbite design for Investment Firm

We want a basic (clean) website that follows the form, fonts and colors of our attachments. This is for a financial investment management firm, but we have a boutique (anti-Wall Street) approach. Site should have an Home Page (Logo up top - room for basic copy on bottom, Philosophy Page (room for Quarterly Letter attachment and basic copy, Performance Page (room for Performance Overview and Performance Analysis and basic copy), Team Page, Commentary Page and Contact
Updates

Reason: Some designers have asked for an extension. Again, please only use image of Train Station or Train Station Logo in design.

Target Market(s)

Small and mid-size financial advisors from across the country

Industry/Entity Type

Financial

Number of Pages Required

5+ page

Font styles to use
Other font styles liked:
• Palotino Linotype

Colors
3176b5
cfdeed
ffffff

Requirements
Must have
• Please refer to existing site www.qarvelton.com. Of note, this is too complex / cluttered. We simply want Blur, Grey and White consistent with attachments. The copy is pretty good, but will be simplified (and no quotes)
Should not have
• No images other than train station logo and / or train station image

```html
<!DOCTYPE html>
<html lang="en">
<head>
<meta charset="utf-8">
<title>Hollis Street Investment Company</title>
<link href="https://fonts.googleapis.com/css2?family=Open+Sans:wght@400;600;700&display=swap" rel="stylesheet">
<style>
:root{
  --blue:#3176b5;
  --blue-dark:#235a8c;
  --blue-light:#cfdeed;
  --navy:#1f2d55;
  --white:#ffffff;
  --grey-bg:#f3f4f6;
  --grey-line:#dfe3e8;
  --text:#333a44;
  --muted:#8a929c;
  --green:#33b36b;
  --green-soft:#dff3e7;
}
*{box-sizing:border-box;margin:0;padding:0}
html,body{width:1200px;height:2792px;overflow:hidden}
body{font-family:"Open Sans",Arial,sans-serif;color:var(--text);background:var(--white);position:relative}
.abs{position:absolute}

/* header */
.site-header{top:0;left:0;width:1200px;height:112px;background:var(--white)}
.brand{left:40px;top:24px}
.brand-name{font-weight:700;font-size:26px;color:var(--blue);line-height:1.1}
.brand-tag{margin-top:6px;font-size:15px;font-weight:600;color:var(--muted)}
.header-art{left:640px;top:0;width:420px;height:112px;background:linear-gradient(90deg,#fff 0%,#e4ecf5 40%,#cfdeed 100%)}
.btn-letter{left:860px;top:44px;width:150px;height:38px;border-radius:6px;background:var(--blue);color:#fff;font-weight:600;font-size:15px;display:flex;align-items:center;justify-content:center}

.main-nav{top:112px;left:0;width:1200px;height:32px;background:var(--blue);display:flex;padding-left:130px;gap:30px;align-items:center}
.main-nav a{color:#fff;text-decoration:none;font-size:14px;font-weight:600}

/* hero */
.hero{top:144px;left:0;width:1200px;height:456px;background:linear-gradient(100deg,#7d858f 0%,#a9b0b8 45%,#d7dbe0 75%,#b6bcc3 100%)}
.hero-copy{left:130px;top:330px;color:#fff}
.hero-copy h1{font-size:34px;font-weight:600;line-height:1.2;width:560px}
.hero-copy p{margin-top:8px;font-size:16px}
.hero-btns{left:130px;top:452px;display:flex;gap:16px}
.btn{height:34px;padding:0 22px;border-radius:4px;background:var(--blue);color:#fff;font-size:13px;font-weight:600;display:flex;align-items:center}

/* dividends */
.section-title{width:1200px;left:0;text-align:center;font-size:30px;font-weight:700}
.div-title{top:648px;color:var(--blue)}
.ticker-row{top:720px;left:135px;width:930px;display:flex;gap:17px}
.ticker{width:172px;height:118px;border:1px solid var(--grey-line);border-radius:4px;padding:10px 12px;background:#fff;box-shadow:0 1px 3px rgba(0,0,0,.06)}
.ticker-sym{font-weight:700;font-size:16px;color:var(--text)}
.ticker-price{font-size:12px;font-weight:600;color:var(--text)}
.ticker-price span{color:var(--green);font-weight:400;margin-left:6px}
.ticker svg{display:block;margin-top:8px}
.ticker-note{top:862px;left:0;width:1200px;text-align:center;font-size:10px;color:var(--muted);line-height:1.5}

/* ideas */
.ideas{top:1010px;left:135px;width:930px;height:430px;background:var(--grey-bg);border:1px solid var(--grey-line)}
.ideas h2{position:absolute;top:36px;width:100%;text-align:center;font-size:26px;font-weight:700;color:var(--text)}
.ideas .sub{position:absolute;top:76px;width:100%;text-align:center;font-size:12px;color:var(--muted)}
.steps{position:absolute;top:120px;left:40px;width:850px;display:flex;justify-content:space-between}
.step{width:190px;text-align:center}
.step-art{width:96px;height:96px;border-radius:50%;margin:0 auto}
.step h3{margin-top:14px;font-size:11px;font-weight:700;letter-spacing:.5px}
.step p{margin-top:6px;font-size:10px;color:var(--muted);line-height:1.5}
.btn-outline{position:absolute;top:320px;left:385px;width:160px;height:28px;border:1px solid var(--blue);color:var(--blue);font-size:10px;font-weight:600;display:flex;align-items:center;justify-content:center;background:#fff}
.help-band{top:1380px;left:135px;width:930px;height:60px;background:var(--blue);display:flex;justify-content:space-around;align-items:center;color:#fff;font-size:14px;font-weight:600}

/* support */
.support-title{top:1576px;color:var(--text);font-size:28px}
.support-sub{top:1620px;left:0;width:1200px;text-align:center;font-size:12px;color:var(--muted)}
.support-row{top:1680px;left:135px;width:930px;display:flex;justify-content:space-around}
.support-item{width:220px;text-align:center}
.support-icon{width:96px;height:96px;border-radius:50%;background:var(--blue);margin:0 auto;display:flex;align-items:center;justify-content:center}
.support-icon.soft{background:var(--grey-bg);border:1px solid var(--grey-line)}
.support-item h4{margin-top:18px;font-size:14px;font-weight:600}
.support-item p{margin-top:4px;font-size:11px;color:var(--muted)}
.support-item .tag{display:inline-block;margin-top:4px;background:var(--blue);color:#fff;font-size:10px;padding:2px 8px}

/* performance table */
.perf{top:1972px;left:150px;width:900px;border-collapse:collapse;font-size:9.5px}
.perf th{background:var(--navy);color:#fff;font-weight:600;padding:6px 3px}
.perf td{padding:6px 3px;text-align:center;border-bottom:1px solid var(--grey-line)}
.perf td:first-child{text-align:left;font-weight:600;width:120px}
.perf tr.bench td{background:var(--grey-bg);font-weight:700;color:#a33838}
.perf-note{top:2100px;left:150px;font-size:8px;color:var(--muted)}

/* news */
.news{top:2200px;left:0;width:1200px;height:380px;background:var(--grey-bg)}
.feature-art{position:absolute;left:150px;top:40px;width:64px;height:150px;background:linear-gradient(180deg,#cfdeed,#3176b5);border-radius:4px}
.feature{position:absolute;left:232px;top:40px;width:190px}
.feature h3{font-size:19px;font-weight:700;line-height:1.25;color:var(--text)}
.feature p{margin-top:10px;font-size:10px;color:var(--muted);line-height:1.6}
.more{margin-top:14px;font-size:10px;font-weight:700;color:var(--blue);letter-spacing:.5px}
.post{position:absolute;top:40px;width:190px}
.post-kind{font-size:9px;color:var(--muted);display:flex;align-items:center;gap:6px;border-bottom:1px solid var(--grey-line);padding-bottom:8px}
.post-kind i{width:10px;height:10px;background:var(--muted);display:inline-block}
.post h4{margin-top:12px;font-size:15px;font-weight:600;color:var(--blue);line-height:1.3}
.post .date{font-size:9px;color:var(--muted);margin-top:4px}
.post p{margin-top:14px;font-size:10px;color:var(--muted);line-height:1.6}

/* footer */
.site-footer{top:2580px;left:0;width:1200px;height:172px;background:var(--blue)}
.foot-cols{position:absolute;left:150px;top:36px;display:flex;gap:90px}
.foot-col h5{font-size:11px;color:#fff;font-weight:700;margin-bottom:6px}
.foot-col a{display:block;font-size:10px;color:var(--blue-light);text-decoration:none;line-height:1.7}
.social{position:absolute;right:150px;top:36px;display:flex;gap:8px}
.social span{width:24px;height:24px;background:#fff;border-radius:2px}
.copyright{top:2752px;left:0;width:1200px;height:40px;background:var(--blue-dark);color:#fff;font-size:10px;display:flex;align-items:center;justify-content:center}
</style>
</head>
<body>

<header class="abs site-header">
  <div class="abs header-art" role="img" aria-label="Line drawing of the historic train station"></div>
  <div class="abs brand">
    <div class="brand-name">Hollis Street Investment Company</div>
    <div class="brand-tag">Separately Managed Accounts</div>
  </div>
  <div class="abs btn-letter">Advisor's letter</div>
</header>

<nav class="abs main-nav">
  <a href="#">Home</a><a href="#">Philosophy</a><a href="#">Performance</a><a href="#">Team</a><a href="#">Letters</a><a href="#">Commentary</a><a href="#">Contact</a>
</nav>

<section class="abs hero" role="img" aria-label="Black and white photograph of the train station building"></section>
<div class="abs hero-copy">
  <h1>Modern investment advice means having better choies.</h1>
  <p>We do, we do investing</p>
</div>
<div class="abs hero-btns"><span class="btn">Read more</span><span class="btn">Invest here</span></div>

<h2 class="abs section-title div-title">Top five dividend Investment</h2>
<div class="abs ticker-row">
  <div class="ticker"><div class="ticker-sym">ALDN</div><div class="ticker-price">135.65<span>+0.71 (1.3%)</span></div>
    <svg width="148" height="50" viewBox="0 0 148 50"><polygon points="0,40 20,34 40,36 60,24 80,28 100,18 120,22 148,8 148,50 0,50" fill="var(--green-soft)"/><polyline points="0,40 20,34 40,36 60,24 80,28 100,18 120,22 148,8" fill="none" stroke="var(--green)" stroke-width="2"/></svg></div>
  <div class="ticker"><div class="ticker-sym">MRWK</div><div class="ticker-price">135.65<span>+0.71 (1.3%)</span></div>
    <svg width="148" height="50" viewBox="0 0 148 50"><polygon points="0,30 20,36 40,26 60,30 80,20 100,24 120,14 148,16 148,50 0,50" fill="var(--green-soft)"/><polyline points="0,30 20,36 40,26 60,30 80,20 100,24 120,14 148,16" fill="none" stroke="var(--green)" stroke-width="2"/></svg></div>
  <div class="ticker"><div class="ticker-sym">GLNT</div><div class="ticker-price">135.65<span>+0.71 (1.3%)</span></div>
    <svg width="148" height="50" viewBox="0 0 148 50"><polygon points="0,38 20,30 40,32 60,28 80,18 100,22 120,12 148,10 148,50 0,50" fill="var(--green-soft)"/><polyline points="0,38 20,30 40,32 60,28 80,18 100,22 120,12 148,10" fill="none" stroke="var(--green)" stroke-width="2"/></svg></div>
  <div class="ticker"><div class="ticker-sym">ALDN</div><div class="ticker-price">135.65<span>+0.71 (1.3%)</span></div>
    <svg width="148" height="50" viewBox="0 0 148 50"><polygon points="0,34 20,38 40,28 60,32 80,22 100,26 120,16 148,12 148,50 0,50" fill="var(--green-soft)"/><polyline points="0,34 20,38 40,28 60,32 80,22 100,26 120,16 148,12" fill="none" stroke="var(--green)" stroke-width="2"/></svg></div>
  <div class="ticker"><div class="ticker-sym">ALDN</div><div class="ticker-price">135.65<span>+0.71 (1.3%)</span></div>
    <svg width="148" height="50" viewBox="0 0 148 50"><polygon points="0,40 20,32 40,34 60,22 80,26 100,20 120,24 148,10 148,50 0,50" fill="var(--green-soft)"/><polyline points="0,40 20,32 40,34 60,22 80,26 100,20 120,24 148,10" fill="none" stroke="var(--green)" stroke-width="2"/></svg></div>
</div>
<p class="abs ticker-note">Quotes shown are delayed at least 15 minutes. Data is for illustration only.<br>Past performance does not guarantee future results.</p>

<section class="abs ideas">
  <h2>Go from great ideas to great investments</h2>
  <p class="sub">Our tools, info, and insights help you be more efficient, every step of trade.</p>
  <div class="steps">
    <div class="step"><div class="step-art" role="img" aria-label="Illustration of a lightbulb idea" style="background:radial-gradient(circle,#cfdeed,#e9eef4)"></div><h3>FIND A GREAT IDEA</h3><p>Research and compare investment products with simple screens.</p></div>
    <div class="step"><div class="step-art" role="img" aria-label="Illustration of testing a strategy" style="background:radial-gradient(circle,#dff3e7,#e9eef4)"></div><h3>TEST IT OUT</h3><p>Try strategies with sample data before you commit real money.</p></div>
    <div class="step"><div class="step-art" role="img" aria-label="Illustration of executing a plan" style="background:radial-gradient(circle,#f6e3c9,#e9eef4)"></div><h3>EXECUTE THE PLAN</h3><p>Place trades quickly with clear pricing and steady support.</p></div>
    <div class="step"><div class="step-art" role="img" aria-label="Illustration of monitoring investments" style="background:radial-gradient(circle,#cfdeed,#e9eef4)"></div><h3>KEEP IT ON YOUR RADAR</h3><p>Track your positions and receive alerts when markets move.</p></div>
  </div>
  <div class="btn-outline">LEARN MORE ABOUT TRADING</div>
</section>
<div class="abs help-band"><span>Get real help from real humans</span><span>Call anytime : 1-800-123-4567</span><span>Go live chat with a representative</span></div>

<h2 class="abs section-title support-title">We're here to help-however and whenever you need it</h2>
<p class="abs support-sub">No matter what financial questions you have, we're here to work with you on your terms.</p>
<div class="abs support-row">
  <div class="support-item"><div class="support-icon"><svg width="40" height="40" viewBox="0 0 24 24"><path fill="#fff" d="M6.6 10.8a15.2 15.2 0 0 0 6.6 6.6l2.2-2.2c.3-.3.7-.4 1-.2 1.1.4 2.3.6 3.6.6.6 0 1 .4 1 1V20c0 .6-.4 1-1 1A17 17 0 0 1 3 4c0-.6.4-1 1-1h3.5c.6 0 1 .4 1 1 0 1.3.2 2.5.6 3.6.1.3 0 .7-.2 1z"/></svg></div><h4>Questions?</h4><span class="tag">1-800-123-4567</span></div>
  <div class="support-item"><div class="support-icon soft"><svg width="40" height="40" viewBox="0 0 24 24"><path fill="#3176b5" d="M4 4h16a1 1 0 0 1 1 1v10a1 1 0 0 1-1 1H9l-5 4V5a1 1 0 0 1 1-1z"/></svg></div><h4>Chat with our</h4><p>Representative team</p></div>
  <div class="support-item"><div class="support-icon"><svg width="40" height="40" viewBox="0 0 24 24"><path fill="#fff" d="M5 3h14v18h-5v-4h-4v4H5zM8 6v2h2V6zm6 0v2h2V6zM8 10v2h2v-2zm6 0v2h2v-2z"/></svg></div><h4>Find an Fine</h4><p>Investor center</p></div>
</div>

<table class="abs perf">
  <tr><th></th><th>2003</th><th>2004</th><th>2005</th><th>2006</th><th>2007</th><th>2008</th><th>2009</th><th>2010</th><th>2011</th><th>2012</th><th>2013</th><th>2014</th><th>2015</th><th>2016</th><th>2017</th></tr>
  <tr><td>Core Equity – Gross</td><td>31.2%</td><td>14.3%</td><td>5.1%</td><td>9.9%</td><td>11.1%</td><td>-19.8%</td><td>24.9%</td><td>9.2%</td><td>6.4%</td><td>12.8%</td><td>25.6%</td><td>11.9%</td><td>1.8%</td><td>5.6%</td><td>19.2%</td></tr>
  <tr><td>Core Equity – Net</td><td>30.1%</td><td>13.2%</td><td>4.1%</td><td>8.9%</td><td>10.0%</td><td>-20.6%</td><td>23.7%</td><td>8.1%</td><td>5.4%</td><td>11.7%</td><td>24.4%</td><td>10.8%</td><td>0.8%</td><td>4.6%</td><td>18.1%</td></tr>
  <tr class="bench"><td>Broad Mkt TR</td><td>28.7%</td><td>10.9%</td><td>4.9%</td><td>15.8%</td><td>5.5%</td><td>-37.0%</td><td>26.5%</td><td>15.1%</td><td>2.1%</td><td>16.0%</td><td>32.4%</td><td>13.7%</td><td>1.4%</td><td>12.0%</td><td>21.8%</td></tr>
</table>
<p class="abs perf-note">Net of fees. See disclosures.</p>

<section class="abs news">
  <div class="feature-art" role="img" aria-label="Illustration of an advisor looking ahead"></div>
  <div class="feature"><h3>What just happened. And what comes next.</h3><p>Our latest view on markets, from rate decisions to earnings, and what it means for clients.</p><div class="more">READ MORE</div></div>
  <div class="post" style="left:470px"><div class="post-kind"><i></i>VIDEO</div><h4>Now in Online Investing</h4><div class="date">Sep 21, 2017</div><p>A short guide to opening an account and building a plan that fits your goals online.</p><div class="more">READ MORE</div></div>
  <div class="post" style="left:680px"><div class="post-kind"><i></i>ARTICLE</div><h4>Creating an Investment Portfolio</h4><div class="date">Sep 18, 2017</div><p>How we blend quality stocks and patient cash to balance growth with steady income.</p><div class="more">READ MORE</div></div>
  <div class="post" style="left:890px"><div class="post-kind"><i></i>VIDEO</div><h4>Growing As Income</h4><div class="date">Sep 12, 2017</div><p>Why dividend growth matters and how reinvesting builds lasting value over time.</p><div class="more">READ MORE</div></div>
</section>

<footer class="abs site-footer">
  <div class="foot-cols">
    <div class="foot-col"><h5>About us</h5><a href="#">Demo1</a><a href="#">Demo1</a><a href="#">Demo1</a><a href="#">Demo1</a></div>
    <div class="foot-col"><h5>About us</h5><a href="#">Demo1</a><a href="#">Demo1</a><a href="#">Demo1</a><a href="#">Demo1</a></div>
    <div class="foot-col"><h5>About us</h5><a href="#">Demo1</a><a href="#">Demo1</a><a href="#">Demo1</a><a href="#">Demo1</a></div>
    <div class="foot-col"><h5>About us</h5><a href="#">Demo1</a><a href="#">Demo1</a><a href="#">Demo1</a><a href="#">Demo1</a></div>
  </div>
  <div class="social"><span></span><span></span><span></span><span></span></div>
</footer>
<div class="abs copyright">© Copyright By Hollis Street Investment Company</div>

</body>
</html>
```